Business card and (possibly) logo

Hi - we need a new business card.
We have an existing logo that we quite like but we are open to options.
We are an architectural firm - we specialize in upmarket residential work and apartment blocks.
We are chasing a business card at present but also want to extensively update our website going forward to attract a much higher level of client / investor / developer.
Our current logo is black, grey and yellow and based on the sun/moon temples in Mexico.
We are open to variations.
We want to communicate professionalism, trust, quality.
Our website is www.corvelldesignhouse.com.au - but note as above - we want to change the website as well to be a lot 'classier' and to appeal to a higher end market.

thanks

Target Market(s)

We are an architect firm - our target market is Developers and builders of high end houses and luxury apartment blocks. Also private home owners wanting to build excellent expensive houses. (ideally over $1m budgets)

Industry/Entity Type

Residential

Requirements
Must have
• Logo
Contact details;
Name
phone, mobile, email, web

```html
<!DOCTYPE html>
<html lang="en">
<head>
<meta charset="utf-8">
<title>Corvell Design House — Business Cards</title>
<link rel="stylesheet" href="https://fonts.googleapis.com/css2?family=Syncopate:wght@400;700&display=swap">
<style>
  :root {
    --page: #ffffff;
    --navy: #0c2e4f;
    --navy-edge: #000000;
    --silver: #b8b8b8;
    --tan: #c4b090;
    --grey-text: #a6a6a6;
    --frame: #c9bda4;
    --frame-outer: #d2d2d2;
  }
  * { margin: 0; padding: 0; box-sizing: border-box; }
  html, body {
    width: 1200px; height: 963px; overflow: hidden;
    background: var(--page);
    font-family: "Syncopate", "Arial", sans-serif;
  }
  .canvas { position: relative; width: 1200px; height: 963px; }

  .card { position: absolute; }
  .card--dark {
    left: 12px; top: 6px; width: 535px; height: 936px;
    background: var(--navy);
    border: 2px solid var(--navy-edge);
    color: var(--silver);
  }
  .card--light {
    left: 649px; top: 0; width: 545px; height: 958px;
    background: var(--page);
    border: 2px solid var(--frame-outer);
    color: var(--grey-text);
  }
  .card--light .inner-frame {
    position: absolute; left: 14px; top: 16px; right: 14px; bottom: 16px;
    border: 2px solid var(--frame);
  }

  .brand {
    position: absolute; left: 58px; top: 68px;
    display: flex; align-items: center; gap: 22px;
    color: var(--tan);
  }
  .brand__dot {
    width: 104px; height: 104px; border-radius: 50%;
    background: var(--tan); flex: none;
  }
  .brand__name {
    font-size: 30px; font-weight: 400; line-height: 1.35;
    letter-spacing: 3px; text-transform: uppercase;
  }

  .contact {
    position: absolute; left: 86px; top: 478px;
    font-variant: small-caps; letter-spacing: 3px;
  }
  .contact__name { font-size: 38px; line-height: 1; letter-spacing: 4px; margin-bottom: 22px; }
  .contact__role { font-size: 27px; line-height: 1; margin-bottom: 14px; }
  .contact__phone { font-size: 26px; line-height: 1; margin-bottom: 14px; }
  .contact__email { font-size: 21px; line-height: 1; }

  .office {
    position: absolute; left: 0; right: 0; top: 780px;
    text-align: center; color: var(--tan);
    font-variant: small-caps; letter-spacing: 3px;
    font-size: 22px; line-height: 32px;
  }
</style>
</head>
<body>
<main class="canvas">

  <section class="card card--dark" aria-label="Business card, navy version">
    <div class="brand">
      <span class="brand__dot"></span>
      <span class="brand__name">Corvell<br>Design House</span>
    </div>
    <div class="contact">
      <p class="contact__name">Daniel Hart</p>
      <p class="contact__role">Serior Architech</p>
      <p class="contact__phone">002-417-530-2684</p>
      <p class="contact__email">Daniel@CorvellDH.com</p>
    </div>
    <address class="office" style="font-style:normal">
      Maine Office<br>
      002-417-530-1190<br>
      4418 Harlow Lane<br>
      Kestrel Bay, Australia 98720
    </address>
  </section>

  <section class="card card--light" aria-label="Business card, white version">
    <div class="inner-frame"></div>
    <div class="brand">
      <span class="brand__dot"></span>
      <span class="brand__name">Corvell<br>Design House</span>
    </div>
    <div class="contact">
      <p class="contact__name">Daniel Hart</p>
      <p class="contact__role">Serior Architech</p>
      <p class="contact__phone">002-417-530-2684</p>
      <p class="contact__email">Daniel@CorvellDH.com</p>
    </div>
    <address class="office" style="font-style:normal">
      Maine Office<br>
      002-417-530-1190<br>
      4418 Harlow Lane<br>
      Kestrel Bay, Australia 98720
    </address>
  </section>

</main>
</body>
</html>
```